Business card design for Automotive workshop

We need a business card for a new automotive repair and tyre shop called Keelstone Prime Automotive located in New Zealand. We are a clean, modern and fresh workshop and company.

Front needs to feature logo,
my name:
Marlo Fitzgerald (director)

Address:
42 Tamsin Road
Harlow Bay 3592

Phone: 07 541 2298
Mobile: 027 419 5073
Email: office@keelstoneautomotive.co.nz
Website: keelstoneautomotive.co.nz

Back needs to feature an area to write down appointment details, date and time.

Also feature a list of jobs and work we do such as,
Vehicle Servicing
All Mechanical Repairs
Warrant of Fitness
Tyres & Wheel Alignments
Automotive Diagnostics
Automotive Parts & Supplies

```html
<!DOCTYPE html>
<html lang="en">
<head>
<meta charset="utf-8">
<title>Keelstone Prime Automotive – Business Card</title>
<link rel="stylesheet" href="https://fonts.googleapis.com/css2?family=Open+Sans:wght@400;600;700&display=swap">
<style>
  :root {
    --backdrop: #5a5a5d;
    --card: #37363c;
    --card-texture: #3d3c43;
    --band: #050505;
    --red: #e3242b;
    --white: #ffffff;
    --field: #cfcfcf;
  }
  * { box-sizing: border-box; margin: 0; padding: 0; }
  html, body { width: 1200px; height: 814px; overflow: hidden; }
  body {
    background: var(--backdrop);
    font-family: "Open Sans", sans-serif;
    color: var(--white);
    position: relative;
  }
  .card {
    position: absolute;
    top: 252px;
    width: 540px;
    height: 309px;
    background: linear-gradient(160deg, var(--card-texture), var(--card));
    overflow: hidden;
    box-shadow: 0 8px 24px rgba(0,0,0,.45);
  }
  .card--back { left: 40px; }
  .card--front { left: 620px; }

  .brand-name {
    font-weight: 700;
    letter-spacing: 1px;
    color: var(--white);
    text-transform: uppercase;
    white-space: nowrap;
  }

  /* Back side */
  .brand-pill {
    position: absolute;
    left: 95px; top: 38px;
    width: 350px; height: 58px;
    background: var(--band);
    border-radius: 29px;
    display: flex; align-items: center; justify-content: center;
  }
  .brand-pill .brand-name { font-size: 16px; }
  .services {
    position: absolute;
    left: 0; right: 0; top: 118px;
    list-style: none;
    text-align: center;
    font-size: 13px;
    line-height: 24px;
  }
  .services li span::before {
    content: "•";
    color: var(--red);
    margin: 0 3px 0 6px;
  }
  .appointment-band {
    position: absolute;
    left: 0; right: 0; top: 218px;
    height: 50px;
    background: var(--band);
    display: flex; align-items: center; justify-content: center;
    gap: 14px;
  }
  .appointment-field {
    width: 130px; height: 26px;
    border-radius: 13px;
    background: var(--field);
  }
  .appointment-label { font-size: 15px; margin-right: 18px; }

  /* Front side */
  .brand-band { position: absolute; right: 0; top: 0; width: 300px; height: 80px; }
  .brand-band-name {
    position: absolute; right: 0; top: 0;
    width: 282px; height: 80px;
    display: flex; align-items: center; justify-content: center;
  }
  .brand-band-name .brand-name { font-size: 14px; }
  .contact-person { position: absolute; left: 30px; top: 132px; }
  .person-name { font-size: 18px; font-weight: 700; color: var(--red); line-height: 22px; }
  .person-title { font-size: 12px; line-height: 16px; }
  .address-band { position: absolute; left: 0; top: 174px; }
  .address-text {
    position: absolute; left: 30px; top: 174px;
    height: 30px; line-height: 30px;
    font-size: 13px; font-weight: 600;
  }
  .contact-list {
    position: absolute; left: 30px; top: 212px;
    list-style: none; font-size: 13px; line-height: 19px;
  }
  .contact-list li { display: flex; align-items: center; gap: 8px; }
  .contact-list svg { flex: none; }
</style>
</head>
<body>

<section class="card card--back" aria-label="Card back">
  <div class="brand-pill"><span class="brand-name">Keelstone Prime Automotive</span></div>
  <ul class="services">
    <li><span>Vehicle Servicing</span><span>All Mechanical Repairs</span></li>
    <li><span>Warrant of Fitness</span><span>Tyres &amp; Wheel Alignments</span></li>
    <li><span>Automotive Diagnostics</span><span>Automotive Parts &amp; Supplies</span></li>
  </ul>
  <div class="appointment-band">
    <div class="appointment-field"></div><span class="appointment-label">Time</span>
    <div class="appointment-field"></div><span class="appointment-label">Date</span>
  </div>
</section>

<section class="card card--front" aria-label="Card front">
  <svg class="brand-band" width="300" height="80" viewBox="0 0 300 80">
    <polygon points="40,0 300,0 300,80 18,80 0,40" fill="var(--band)"/>
  </svg>
  <div class="brand-band-name"><span class="brand-name">Keelstone Prime Automotive</span></div>

  <div class="contact-person">
    <div class="person-name">Marlo Fitzgerald</div>
    <div class="person-title">Managing Director</div>
  </div>

  <svg class="address-band" width="360" height="30" viewBox="0 0 360 30">
    <polygon points="0,0 345,0 330,30 0,30" fill="var(--red)"/>
  </svg>
  <div class="address-text">42 Tamsin Road, Harlow Bay 3592</div>

  <ul class="contact-list">
    <li><svg width="11" height="11" viewBox="0 0 11 11"><rect width="11" height="11" rx="2" fill="var(--red)"/><rect x="3.5" y="2" width="4" height="7" rx="1" fill="none" stroke="#fff" stroke-width="1"/></svg>+ 027 419 5073</li>
    <li><svg width="11" height="11" viewBox="0 0 11 11"><rect width="11" height="11" rx="2" fill="var(--red)"/><path d="M3 3.5 Q3 8 7.5 8" stroke="#fff" stroke-width="1.4" fill="none"/></svg>+ 07 541 2298</li>
    <li><svg width="11" height="11" viewBox="0 0 11 11"><rect width="11" height="11" rx="2" fill="var(--red)"/><path d="M2.5 3.5h6v4h-6z M2.5 3.5l3 2.2 3-2.2" stroke="#fff" stroke-width="0.9" fill="none"/></svg>office@keelstoneautomotive.co.nz</li>
    <li><svg width="11" height="11" viewBox="0 0 11 11"><rect width="11" height="11" rx="2" fill="var(--red)"/><circle cx="5.5" cy="5.5" r="3" stroke="#fff" stroke-width="0.9" fill="none"/><path d="M2.5 5.5h6" stroke="#fff" stroke-width="0.8"/></svg>keelstoneautomotive.co.nz</li>
  </ul>
</section>

</body>
</html>
```